Square graphic for social media post

I want to create a 1080 x 1080px all-black image for the quote below that I can share on social media. I want the emphasis to be primarily on the quote, secondarily on the portrait, and third (smallest) on the logo. I want the background on the portrait to be edited so it's transparent and just shows the face of the person on a black background (no brick wall visible).

Graphic color: black
Text color: white
Content: "What we went through is going to make the greatest generation of hoteliers our industry has ever seen." << biggest text
Dorian Welk << smaller text
President, Marrowgate Hotels << smaller text
[image of person - use whichever version looks better to you]
[Add Lodging Ledger logo - whichever looks better to you]

This image needs to be readable when sized down much smaller (400x400?) so want the text and portrait to take up most of the space.

I'd like the output both as PNG and original file (preferably Canva). Thanks!

Target Market(s)

Hotel managers

Industry/Entity Type

Hospitality

Font styles to use
Sans Serif

Colors

Designer to choose colors to be used in the design.

Requirements
Must have
• Needs to focus on the quote and the person quoted (the portrait)

```html
<!DOCTYPE html>
<html lang="en">
<head>
<meta charset="utf-8">
<title>Quote card – Dorian Welk</title>
<link rel="stylesheet" href="https://fonts.googleapis.com/css2?family=Montserrat:wght@400;500&family=Playfair+Display:wght@700&display=swap">
<style>
  :root {
    --bg: #0f1011;
    --ink: #ffffff;
    --portrait-light: #2a2a2b;
    --portrait-dark: #1c1c1d;
  }
  * { margin: 0; padding: 0; box-sizing: border-box; }
  html, body {
    width: 1200px;
    height: 1200px;
    overflow: hidden;
    background: var(--bg);
  }
  .quote-card {
    position: relative;
    width: 1200px;
    height: 1200px;
    background: var(--bg);
    color: var(--ink);
    font-family: "Montserrat", Arial, sans-serif;
  }
  .brand {
    position: absolute;
    top: 104px;
    left: 0;
    width: 1200px;
    text-align: center;
    font-size: 15px;
    font-weight: 500;
    letter-spacing: 0.32em;
    text-transform: uppercase;
    color: var(--ink);
  }
  .portrait {
    position: absolute;
    left: 412px;
    top: 232px;
    width: 378px;
    height: 378px;
    border-radius: 50%;
    background: radial-gradient(circle at 50% 42%, var(--portrait-light) 0%, var(--portrait-dark) 100%);
  }
  .quote {
    position: absolute;
    left: 200px;
    top: 668px;
    width: 820px;
    text-align: center;
    font-size: 62px;
    font-weight: 400;
    line-height: 75px;
    letter-spacing: 0.005em;
  }
  .quote-mark {
    position: absolute;
    font-family: "Playfair Display", Georgia, serif;
    font-weight: 700;
    font-size: 84px;
    line-height: 1;
    color: var(--ink);
  }
  .quote-mark--open { left: 148px; top: 640px; }
  .quote-mark--close { left: 792px; top: 1015px; }
  .attribution {
    position: absolute;
    left: 240px;
    top: 1092px;
    display: flex;
    align-items: baseline;
    gap: 30px;
    white-space: nowrap;
  }
  .attribution__name {
    font-size: 41px;
    font-weight: 400;
  }
  .attribution__role {
    font-size: 27px;
    font-weight: 400;
  }
</style>
</head>
<body>
  <main class="quote-card">
    <div class="brand">Lodging Ledger</div>

    <div class="portrait" role="img" aria-label="Head-and-shoulders portrait of Dorian Welk, smiling, in a navy blazer and white shirt, on a dark background"></div>

    <span class="quote-mark quote-mark--open" aria-hidden="true">&ldquo;</span>
    <blockquote class="quote">
      What we went through is<br>
      going to make the<br>
      greatest generation of<br>
      hoteliers our industry has<br>
      ever seen.
    </blockquote>
    <span class="quote-mark quote-mark--close" aria-hidden="true">&rdquo;</span>

    <p class="attribution">
      <span class="attribution__name">Dorian Welk</span>
      <span class="attribution__role">President, Marrowgate Hotels</span>
    </p>
  </main>
</body>
</html>
```